Moving offices: new address and other details notification postcard

We are a small firm of accountants moving offices for the first time in 30 years. The project is to produce a postcard that we can send to customers, suppliers and other business contacts letting them know that we are moving and advising our new address.. Attached is our logo and also a sketch we found through google of Tarrow Vale Parade in London which is where we are moving to and we thought might be a suitable as part of the card. Ideally we want something that will communicate our new contact details and from which people will update there systems rather than simply just file the card in the bin!
I understand that the card may need to be mailed in an envelope to stop Crestline Post returning it like a boomerang.
Our website is
www.quellinandco.biz

```html
<!DOCTYPE html>
<html lang="en">
<head>
<meta charset="utf-8">
<title>Quellin and Co have moved – postcard</title>
<link rel="stylesheet" href="https://fonts.googleapis.com/css2?family=Lobster&family=Open+Sans:wght@400;600;700&family=Oswald:wght@500&display=swap">
<style>
  :root {
    --paper: #ffffff;
    --ink: #333333;
    --brand-red: #c2444b;
    --badge-red: #b0434a;
    --title-red: #9a2e3a;
    --rule: #9a9a9a;
    --band: #000000;
    --sketch-light: #f6e4ea;
    --sketch-mid: #d9aabb;
    --sketch-deep: #8e5d7c;
  }
  * { margin: 0; padding: 0; box-sizing: border-box; }
  html, body { width: 720px; height: 1200px; overflow: hidden; background: var(--paper); }
  body { position: relative; font-family: "Open Sans", sans-serif; color: var(--ink); }

  .card-back { position: absolute; left: 0; top: 0; width: 720px; height: 540px; background: var(--paper); }
  .brand-name {
    position: absolute; left: 40px; top: 34px;
    font-family: "Lobster", cursive; font-size: 34px; color: var(--brand-red); font-weight: 400;
  }
  .badge { position: absolute; }
  .badge svg { position: absolute; inset: 0; width: 100%; height: 100%; }
  .badge-text {
    position: absolute; inset: 0; display: flex; align-items: center; justify-content: center;
    text-align: center; color: #fff; font-family: "Oswald", sans-serif; font-weight: 500;
    text-transform: uppercase; line-height: 1.25;
  }
  .badge-back { left: 88px; top: 107px; width: 160px; height: 160px; }
  .badge-back .badge-text { font-size: 19px; letter-spacing: .5px; }

  .new-address { position: absolute; left: 60px; top: 280px; width: 300px; }
  .new-address-heading { font-family: "Lobster", cursive; font-weight: 400; font-size: 30px; color: var(--brand-red); }
  .address-lines { margin-top: 8px; font-size: 17px; font-weight: 700; line-height: 1.35; font-style: normal; color: var(--ink); }
  .contact { margin-top: 14px; font-size: 14px; line-height: 1.45; color: var(--brand-red); }
  .contact .web { font-size: 18px; font-weight: 700; }

  .stamp-box { position: absolute; left: 576px; top: 29px; width: 102px; height: 104px; border: 2px solid #b5b5b5; }
  .address-rule { position: absolute; left: 384px; width: 312px; height: 0; border-top: 2px solid var(--rule); }

  .divider-band { position: absolute; left: 0; top: 540px; width: 720px; height: 84px; background: var(--band); }

  .card-front { position: absolute; left: 0; top: 624px; width: 720px; height: 576px; background: var(--paper); }
  .street-sketch {
    position: absolute; left: 0; top: 0; width: 720px; height: 504px;
    background:
      radial-gradient(ellipse at 75% 45%, rgba(255,240,215,.9), rgba(255,240,215,0) 45%),
      linear-gradient(90deg, var(--sketch-deep) 0%, var(--sketch-mid) 22%, var(--sketch-light) 45%, var(--sketch-light) 60%, var(--sketch-mid) 82%, var(--sketch-deep) 100%);
  }
  .sketch-edge { position: absolute; left: 0; top: 440px; width: 720px; height: 70px; }
  .front-title {
    position: absolute; left: 0; top: 44px; width: 720px; text-align: center;
    font-family: "Lobster", cursive; font-weight: 400; font-size: 62px; line-height: 1.3; color: var(--title-red);
  }
  .badge-front { left: 586px; top: 366px; width: 134px; height: 134px; }
  .badge-front .badge-text { font-size: 13px; }
  .front-footer { position: absolute; left: 0; top: 514px; width: 720px; text-align: center; font-size: 13px; line-height: 1.6; color: var(--ink); }
  .front-footer .accent { color: var(--brand-red); }
  .front-footer strong { font-weight: 700; }
</style>
</head>
<body>
<svg width="0" height="0" style="position:absolute">
  <defs>
    <symbol id="starburst" viewBox="-100 -100 200 200">
      <polygon points="100,0 86.3,17.2 92.4,38.3 73.1,48.9 70.7,70.7 48.9,73.1 38.3,92.4 17.2,86.3 0,100 -17.2,86.3 -38.3,92.4 -48.9,73.1 -70.7,70.7 -73.1,48.9 -92.4,38.3 -86.3,17.2 -100,0 -86.3,-17.2 -92.4,-38.3 -73.1,-48.9 -70.7,-70.7 -48.9,-73.1 -38.3,-92.4 -17.2,-86.3 0,-100 17.2,-86.3 38.3,-92.4 48.9,-73.1 70.7,-70.7 73.1,-48.9 92.4,-38.3 86.3,-17.2" fill="currentColor"/>
    </symbol>
  </defs>
</svg>

<section class="card-back">
  <div class="brand-name">Quellin and Co</div>
  <div class="badge badge-back">
    <svg style="color:var(--badge-red)"><use href="#starburst"/></svg>
    <div class="badge-text">Please<br>update your<br>records</div>
  </div>
  <div class="new-address">
    <h2 class="new-address-heading">With our new address</h2>
    <address class="address-lines">Suites 3 and 4,<br>63-67 Larkspur Place,<br>Tarrow Vale, London, N14 7QD.</address>
    <p class="contact">Tel: (0)20 7946 0321<br>enquiries@quellinandco.biz<br><span class="web">www.quellinandco.biz</span></p>
  </div>
  <div class="stamp-box"></div>
  <div class="address-rule" style="top:252px"></div>
  <div class="address-rule" style="top:302px"></div>
  <div class="address-rule" style="top:356px"></div>
  <div class="address-rule" style="top:408px"></div>
</section>

<div class="divider-band"></div>

<section class="card-front">
  <div class="street-sketch" role="img" aria-label="Pastel pink sketch of Tarrow Vale Parade street with terraced buildings and a church spire"></div>
  <svg class="sketch-edge" viewBox="0 0 720 70" preserveAspectRatio="none">
    <path d="M0,64 Q360,20 720,40 L720,70 L0,70 Z" fill="#ffffff"/>
  </svg>
  <h1 class="front-title">Quellin and Co<br>have moved</h1>
  <div class="badge badge-front">
    <svg style="color:var(--title-red)"><use href="#starburst"/></svg>
    <div class="badge-text">Please<br>update your<br>records</div>
  </div>
  <p class="front-footer">
    New Address: <span class="accent">Suites 3 and 4, 63-67 Larkspur Place, Tarrow Vale, London, N14 7QD</span><br>
    Tel: <strong class="accent">(0)20 7946 0321</strong> – enquiries@quellinandco.biz – <span class="accent">www.quellinandco.biz</span>
  </p>
</section>
</body>
</html>
```